"Brelunda" sparkling beverage

Dear All!
I need a stick label (82*95 - front label, 82*65 - back label )design for а sparkling beverage, name is "Brelunda", 4 flavours: lemonade,duchess pear, estragon, original. Transparent glass bottles 0,5 liter (alumnium closure 28*15)/0,33 liter (crown cap), neck label should also be on the bottle 0,5 liter.
European style is welcomed
Do not send the disigns with a little changes several times, please!!!
Target Market(s)
Young people from 12-30 ages old
Look and feel
Each slider illustrates characteristics of the customer's brand and the style your logo design should communicate.

```html
<!DOCTYPE html>
<html lang="en">
<head>
<meta charset="utf-8">
<title>Brelunda Sparkling Beverage – Label Set</title>
<link rel="stylesheet" href="https://fonts.googleapis.com/css2?family=Playfair+Display:wght@700&family=Raleway:wght@400&family=Libre+Baskerville:wght@700&display=swap">
<style>
  :root {
    --page: #ffffff;
    --label-cream: #fcf0cc;
    --frame-line: #c4a273;
    --frame-line-dark: #a8825a;
    --ink: #2a2a2a;
    --flavour-red: #7a1b1b;
  }
  html, body {
    margin: 0;
    padding: 0;
    overflow: hidden;
    background: var(--page);
  }
  .canvas {
    position: relative;
    width: 1200px;
    height: 848px;
    overflow: hidden;
    background: var(--page);
  }
  .neck-label {
    position: absolute;
    left: 262px;
    top: 126px;
    width: 152px;
    height: 532px;
  }
  .front-label {
    position: absolute;
    left: 476px;
    top: 274px;
    width: 462px;
    height: 302px;
  }
  .label-body { fill: var(--label-cream); }
  .frame-line { fill: none; stroke: var(--frame-line); stroke-width: 1; }
  .frame-line-strong { fill: none; stroke: var(--frame-line-dark); stroke-width: 1.4; }
  .brand-name {
    font-family: "Playfair Display", "Didot", serif;
    font-weight: 700;
    font-size: 62px;
    letter-spacing: 5px;
    fill: var(--ink);
  }
  .product-type {
    font-family: "Raleway", "Helvetica", sans-serif;
    font-weight: 400;
    font-size: 19px;
    letter-spacing: 2.8px;
    fill: var(--ink);
  }
  .flavour-name {
    font-family: "Libre Baskerville", "Georgia", serif;
    font-weight: 700;
    font-size: 17px;
    letter-spacing: 4px;
    fill: var(--flavour-red);
  }
  .flavour-initial {
    font-family: "Libre Baskerville", "Georgia", serif;
    font-weight: 700;
    font-size: 40px;
    fill: var(--flavour-red);
  }
</style>
</head>
<body>
<main class="canvas">

  <svg class="neck-label" viewBox="0 0 152 532" aria-label="Neck label, flavour Original">
    <rect class="label-body" x="34" y="0" width="85" height="420"/>
    <circle class="label-body" cx="76" cy="458" r="74"/>
    <path class="frame-line" d="M44 10 H109 V398 A62 62 0 1 1 44 398 Z"/>
    <path class="frame-line" d="M48 14 H105 V402 A57 57 0 1 1 48 402 Z"/>
    <circle class="frame-line-strong" cx="76" cy="458" r="34"/>
    <text class="flavour-initial" x="76" y="472" text-anchor="middle">O</text>
  </svg>

  <svg class="front-label" viewBox="0 0 462 302" aria-label="Front label, Brelunda sparkling beverage, Original">
    <path class="label-body" d="M28 0 H434 A28 28 0 0 0 462 28 V274 A28 28 0 0 0 434 302 H28 A28 28 0 0 0 0 274 V28 A28 28 0 0 0 28 0 Z"/>
    <path class="frame-line" d="M36.7 10 H425.3 A38 38 0 0 0 452 36.7 V265.3 A38 38 0 0 0 425.3 292 H36.7 A38 38 0 0 0 10 265.3 V36.7 A38 38 0 0 0 36.7 10 Z"/>
    <path class="frame-line" d="M41 16 H421 A44 44 0 0 0 446 41 V261 A44 44 0 0 0 421 286 H41 A44 44 0 0 0 16 261 V41 A44 44 0 0 0 41 16 Z"/>
    <path class="frame-line" d="M44 20 H418 A48 48 0 0 0 442 44 V258 A48 48 0 0 0 418 282 H44 A48 48 0 0 0 20 258 V44 A48 48 0 0 0 44 20 Z"/>

    <text class="brand-name" x="233" y="150" text-anchor="middle">BRELUNDA</text>
    <text class="product-type" x="231" y="178" text-anchor="middle">SPARKLING BEVERAGE</text>

    <g class="flavour-badge">
      <polygon class="frame-line-strong" points="150,206 312,206 334,230 312,254 150,254 128,230"/>
      <polygon class="frame-line" points="154,211 308,211 326,230 308,249 154,249 136,230"/>
      <polygon class="frame-line" points="118,222 126,230 118,238 110,230"/>
      <polygon class="frame-line" points="344,222 352,230 344,238 336,230"/>
      <line class="frame-line" x1="126" y1="230" x2="128" y2="230"/>
      <line class="frame-line" x1="334" y1="230" x2="336" y2="230"/>
      <text class="flavour-name" x="233" y="236" text-anchor="middle">ORIGINAL</text>
    </g>
  </svg>

</main>
</body>
</html>
```